Lantern & Row Theatre Academy Business Card

We need a professional looking card for the Lantern & Row Theatre Academy. The logo is attached.
The owner is: Maribel Quistorp
Phone Number: 303-555-0147
Email: lrtheatreacademy@mailbox-demo.com
Website: lrtheatre-demo.com
Somewhere on the front of the card we would like to see the slogan: Step into the limelight
On the back we would like to see the quote: All the world's a stage. -Edmund Pelgrave
We are open to different colors for the wording or maybe just black. Something that will go well with the logo.
Target Market(s)
Individuals seeking a professional children's theatre.
Industry/Entity Type
Business
Colors
Look and feel

```html
<!DOCTYPE html>
<html lang="en">
<head>
<meta charset="utf-8">
<title>Lantern &amp; Row Theatre Academy – Business Card</title>
<link rel="stylesheet" href="https://fonts.googleapis.com/css2?family=Old+Standard+TT:wght@400;700&family=Playfair+Display:ital@1&display=swap">
<style>
  :root {
    --page-bg: #ffffff;
    --card-white: #ffffff;
    --card-border: #cfcfcf;
    --band-black: #000000;
    --footer-grey: #d9d9db;
    --accent-red: #8b0a0a;
    --ink-dark: #231f20;
    --ink-name: #ffffff;
    --ink-title: #a7a7a9;
    --ink-slogan: #7d7d80;
    --ink-quote-mark: #b9b9bc;
  }
  * { margin: 0; padding: 0; box-sizing: border-box; }
  html, body {
    width: 1200px;
    height: 900px;
    overflow: hidden;
    background: var(--page-bg);
  }
  .canvas {
    position: relative;
    width: 1200px;
    height: 900px;
  }
  .business-card {
    position: absolute;
    left: 215px;
    top: 232px;
    width: 770px;
    height: 428px;
    border: 1px solid var(--card-border);
    border-radius: 52px;
    overflow: hidden;
    background: var(--card-white);
  }
  .brand {
    position: absolute;
    left: 0;
    top: 0;
    width: 100%;
    height: 214px;
    display: flex;
    align-items: center;
    justify-content: center;
    gap: 16px;
  }
  .brand-square {
    width: 34px;
    height: 34px;
    background: var(--accent-red);
    flex: none;
  }
  .brand-name {
    font-family: "Old Standard TT", serif;
    font-weight: 400;
    font-size: 36px;
    line-height: 40px;
    color: var(--ink-dark);
    white-space: nowrap;
  }
  .name-band {
    position: absolute;
    left: 0;
    top: 214px;
    width: 100%;
    height: 104px;
    background: var(--band-black);
    text-align: center;
  }
  .person-name {
    margin-top: 10px;
    font-family: "Old Standard TT", serif;
    font-weight: 400;
    font-size: 40px;
    line-height: 48px;
    color: var(--ink-name);
  }
  .person-title {
    margin-top: -6px;
    font-family: "Playfair Display", serif;
    font-style: italic;
    font-size: 30px;
    line-height: 36px;
    color: var(--ink-title);
  }
  .contact-strip {
    position: absolute;
    left: 0;
    top: 318px;
    width: 100%;
    height: 110px;
    background: var(--footer-grey);
  }
  .contact-list {
    position: absolute;
    left: 40px;
    top: 22px;
    list-style: none;
    font-family: "Old Standard TT", serif;
    font-weight: 700;
    font-size: 16px;
    color: var(--ink-dark);
  }
  .contact-item {
    display: flex;
    align-items: center;
    height: 32px;
  }
  .contact-icon {
    width: 28px;
    height: 22px;
    margin-right: 8px;
    fill: var(--accent-red);
  }
  .slogan {
    position: absolute;
    left: 432px;
    top: 30px;
    font-family: "Playfair Display", serif;
    font-style: italic;
    font-size: 28px;
    color: var(--ink-slogan);
    white-space: nowrap;
  }
  .slogan .quote-mark {
    position: absolute;
    left: -32px;
    top: -20px;
    font-size: 64px;
    font-style: normal;
    color: var(--ink-quote-mark);
  }
  .slogan .slogan-text {
    position: relative;
    top: 6px;
  }
</style>
</head>
<body>
<main class="canvas">
  <section class="business-card">
    <header class="brand">
      <div class="brand-square"></div>
      <h1 class="brand-name">Lantern &amp; Row Theatre Academy</h1>
    </header>

    <div class="name-band">
      <p class="person-name">Maribel Quistorp</p>
      <p class="person-title">Owner</p>
    </div>

    <footer class="contact-strip">
      <ul class="contact-list">
        <li class="contact-item">
          <svg class="contact-icon" viewBox="0 0 24 24" aria-hidden="true">
            <path d="M6.6 2.5 9.4 6.3c.4.6.3 1.3-.2 1.8L7.6 9.6c1.2 2.6 3.3 4.7 5.9 5.9l1.5-1.6c.5-.5 1.2-.6 1.8-.2l3.8 2.8c.6.4.8 1.2.4 1.9l-1.3 2.2c-.5.8-1.4 1.2-2.3 1C9.4 20.2 3.8 14.6 2.4 6.6c-.2-.9.2-1.8 1-2.3l1.3-.8c.7-.4 1.5-.2 1.9.4z"/>
          </svg>
          <span class="contact-text">303-555-0147</span>
        </li>
        <li class="contact-item">
          <svg class="contact-icon" viewBox="0 0 30 20" aria-hidden="true">
            <rect x="1" y="2" width="28" height="17"/>
            <path d="M1 2 15 12 29 2" fill="none" stroke="#d9d9db" stroke-width="1.6"/>
            <path d="M1 19 11 9.5M29 19 19 9.5" fill="none" stroke="#d9d9db" stroke-width="1.2"/>
          </svg>
          <span class="contact-text">lrtheatreacademy@mailbox-demo.com</span>
        </li>
      </ul>
      <p class="slogan"><span class="quote-mark">&ldquo;</span><span class="slogan-text">Step into the limelight</span></p>
    </footer>
  </section>
</main>
</body>
</html>
```